Etiketten für selbst erzeugten Obstbrand und Liköre
Zielgruppe
Freunde und Bekannte
Aufgabenstellung
Die Etiketten kommen auf Flaschen, die selbst erzeugten Obstbrand und Liköre enthalten. Das Etikett sollte modern, ohne Schnickschnack und edel aussehen. Das Etikett sollte nur aus grafischen Elementen und Schrift bestehen (keine Bilder/Fotos). Die Schnapssorte selbst trage ich auf einem reservierten Feld handschriftlich auf dem Etikett ein. Es sollte maximal 7cm hoch und 10cm breit sein. Die Flaschen werden ausschließlich verschenkt.

```html
<!DOCTYPE html>
<html lang="de">
<head>
<meta charset="utf-8">
<title>Mirko's Klare Geister – Etikett</title>
<link rel="stylesheet" href="https://fonts.googleapis.com/css2?family=Archivo+Black&display=swap">
<style>
  :root {
    --backdrop: #e4e3e0;
    --label-paper: #efeeea;
    --label-edge: #d8d6d1;
    --ink: #262626;
    --rule: #3a3a3a;
  }
  * { margin: 0; padding: 0; box-sizing: border-box; }
  html, body {
    width: 1200px;
    height: 1200px;
    overflow: hidden;
    background: var(--backdrop);
  }
  .canvas {
    width: 1200px;
    height: 1200px;
    display: flex;
    align-items: center;
    justify-content: center;
  }
  .label {
    position: relative;
    width: 720px;
    height: 920px;
    background: var(--label-paper);
    border: 1px solid var(--label-edge);
    box-shadow: 0 6px 24px rgba(0, 0, 0, 0.08);
  }
  .brand-title {
    position: absolute;
    left: 84px;
    top: 128px;
    font-family: "Archivo Black", sans-serif;
    font-weight: 400;
    font-size: 70px;
    line-height: 1.45;
    letter-spacing: 0.04em;
    text-transform: uppercase;
    color: var(--ink);
  }
  .brand-title span { display: block; }
  .variety-field {
    position: absolute;
    left: 84px;
    bottom: 90px;
    width: 514px;
    height: 30px;
  }
</style>
</head>
<body>
  <main class="canvas">
    <section class="label">
      <h1 class="brand-title">
        <span>Mirko’s</span>
        <span>Klare</span>
        <span>Geister</span>
      </h1>
      <svg class="variety-field" viewBox="0 0 514 30" aria-label="Feld für die handschriftliche Sorte">
        <path d="M2 6 Q 257 26 512 4" fill="none" stroke="var(--rule)" stroke-width="2.2" stroke-linecap="round"/>
      </svg>
    </section>
  </main>
</body>
</html>
```